Basic business card

use my newly created logo - and the phrases (Faster Test Cycles & Smarter Silicon Product Launches) - and my new email domain / ID - use at conferences / tradeshows

Industry/Entity Type

semiconductor

Contact Information for Business Card

Dale J Whitcomb, Owner, communicate via Logo - Lower COT - Cost of Test, Accelerated NPI - New Product Introduction, phone +1 555 014 6208, Chandler, Arizona, USA, dale.whitcomb@vexlora.com

Font styles to use
Sans Serif

Requirements
Nice to have
• re-use my logo created via Pixel Harbor last August (#6182935)

```html
<!DOCTYPE html>
<html lang="en">
<head>
<meta charset="utf-8">
<title>Vexlora Business Card</title>
<link rel="stylesheet" href="https://fonts.googleapis.com/css2?family=Montserrat:wght@400;500;700&family=Oswald:wght@500&display=swap">
<style>
  :root {
    --backdrop: #3b3c3e;
    --paper: #ffffff;
    --navy: #2f4566;
    --ink: #1d1f24;
    --cyan: #14a6dc;
    --blue: #0f6fb8;
    --night-top: #2c3d50;
    --night-bottom: #0d1620;
    --steel: #aebfd3;
  }
  * { box-sizing: border-box; margin: 0; padding: 0; }
  html, body { width: 1200px; height: 1200px; overflow: hidden; }
  body {
    background: var(--backdrop);
    display: flex;
    flex-direction: column;
    align-items: center;
    justify-content: center;
    gap: 80px;
    font-family: "Montserrat", sans-serif;
  }
  .card {
    position: relative;
    width: 700px;
    height: 400px;
    border-radius: 28px;
    overflow: hidden;
  }
  .card-front { background: var(--paper); }
  .card-back {
    background: radial-gradient(ellipse at 55% 35%, var(--night-top), var(--night-bottom) 80%);
    display: flex;
    align-items: center;
    justify-content: center;
  }
  .brand {
    display: flex;
    align-items: center;
    gap: 16px;
    font-family: "Montserrat", sans-serif;
    font-weight: 500;
    letter-spacing: 2px;
  }
  .brand-square { width: 40px; height: 40px; }
  .card-front .brand {
    position: absolute;
    top: 70px;
    left: 150px;
    font-size: 64px;
    color: var(--navy);
  }
  .card-front .brand-square { background: var(--navy); }
  .card-back .brand { font-size: 84px; color: var(--steel); }
  .card-back .brand-square { background: var(--steel); width: 52px; height: 52px; }
  .contact {
    position: absolute;
    left: 60px;
    top: 215px;
  }
  .full-name {
    font-weight: 700;
    font-size: 34px;
    color: var(--cyan);
    line-height: 1;
  }
  .position {
    font-weight: 400;
    font-size: 18px;
    color: var(--ink);
    letter-spacing: 1px;
    margin-top: 4px;
  }
  .email {
    display: flex;
    align-items: center;
    gap: 12px;
    margin-top: 10px;
    font-size: 19px;
    color: var(--ink);
    letter-spacing: 0.5px;
  }
  .tagline {
    position: absolute;
    left: 60px;
    right: 40px;
    bottom: 30px;
    font-family: "Oswald", sans-serif;
    font-weight: 500;
    font-size: 19px;
    color: var(--navy);
    letter-spacing: 0.3px;
    white-space: nowrap;
  }
  .accent-band {
    position: absolute;
    left: 0;
    right: 0;
    bottom: 0;
    height: 70px;
  }
</style>
</head>
<body>
  <section class="card card-front">
    <div class="brand"><span class="brand-square"></span>Vexlora</div>

    <div class="contact">
      <p class="full-name">FULL NAME</p>
      <p class="position">POSITION</p>
      <p class="email">
        <svg width="26" height="18" viewBox="0 0 26 18" aria-hidden="true">
          <rect x="0" y="0" width="26" height="18" fill="#14a6dc"/>
          <polyline points="0,0 13,10 26,0" fill="none" stroke="#ffffff" stroke-width="2"/>
          <polyline points="0,18 10,8 M16,8 26,18" fill="none" stroke="#ffffff" stroke-width="1.5"/>
        </svg>
        email@company.com
      </p>
    </div>

    <svg class="accent-band" viewBox="0 0 700 70" preserveAspectRatio="none" aria-hidden="true">
      <defs>
        <linearGradient id="bandLight" x1="0" x2="1">
          <stop offset="0" stop-color="#14a6dc"/>
          <stop offset="1" stop-color="#2ab6e6"/>
        </linearGradient>
        <linearGradient id="bandDeep" x1="0" x2="1">
          <stop offset="0" stop-color="#2a86c8"/>
          <stop offset="1" stop-color="#0f6fb8"/>
        </linearGradient>
      </defs>
      <polygon points="0,62 420,58 420,70 0,70" fill="url(#bandLight)"/>
      <polygon points="300,44 420,44 420,70 300,70" fill="url(#bandLight)"/>
      <polygon points="428,40 700,40 700,70 428,70" fill="url(#bandDeep)"/>
    </svg>

    <p class="tagline">FASTER TEST CYCLES &amp; SMARTER SILICON PRODUCT LAUNCHES</p>
  </section>

  <section class="card card-back">
    <div class="brand"><span class="brand-square"></span>Vexlora</div>
  </section>
</body>
</html>
```